Study Lantern

StudyLantern.com will be a place for people looking for information, resources, and advisement to start or continue their education. We want a friendly, inviting site design that makes finding what potential students are looking for simple and easy to navigate. We are not committed to the colors of the logo, so variations on the color scheme are welcome.

Text instructions based on the wireframe: For the site's homepage we'd like a banner at the very top for our Logo and white space to the right of it. See attachments for logo + wireframe. Below that would be navigation. Below that split into 2/3 on the left we would have home page content, and 1/3 on the right we would have the lead form. At the bottom of the page we would have a space for types of degrees, then a footer with copyright info + site info.

See wireframes for additional page layouts.

Industry/Entity Type

Education

Requirements
Must have
• At minimum we are looking for three pages: homepage, choose your degree path page, and content page.
Nice to have
• -White space is appreciated
-Variations on the color scheme are welcome, we are not married to the existing logo's color scheme.

```html
<!DOCTYPE html>
<html lang="en">
<head>
<meta charset="utf-8">
<title>Study Lantern – Articles</title>
<link href="https://fonts.googleapis.com/css2?family=Ubuntu:wght@400;500;700&display=swap" rel="stylesheet">
<style>
:root{
  --orange:#e1491d;
  --ink:#3b3b3b;
  --body:#555;
  --nav:#1c1c1c;
  --cream:#f3f0e4;
  --field:#c9c4b4;
  --footer:#3c3c3c;
  --teal:#1f5f6b;
  --link:#1a3fb0;
  --green:#1a9a1a;
}
*{box-sizing:border-box;margin:0;padding:0}
html,body{width:920px;height:1200px;overflow:hidden}
body{position:relative;font-family:Arial,Helvetica,sans-serif;color:var(--body);
  background:linear-gradient(90deg,#d9623a 0%,#e9c9a0 4%,#f1ebe0 7%,#f1ebe0 93%,#d8b2a0 96%,#b83a3a 100%)}
.abs{position:absolute}
.header{left:0;top:0;width:920px;height:93px;background:linear-gradient(#fff,#ececec)}
.logo{left:78px;top:38px;font-family:Ubuntu,sans-serif;font-size:30px;font-weight:500;color:#666;display:flex;align-items:center;gap:8px}
.logo .mark{width:18px;height:18px;background:var(--orange)}
.follow{left:714px;top:11px;font-size:8px;font-weight:bold;color:#555;display:flex;gap:4px;align-items:center}
.follow span.sq{width:14px;height:14px;background:#555;border-radius:2px}
.call{left:676px;top:35px;display:flex;gap:6px;align-items:center}
.call .icon{width:46px;height:48px;background:var(--orange);border:3px solid #fff;border-radius:5px;box-shadow:0 1px 3px #999;display:flex;align-items:center;justify-content:center}
.call .t1{font-family:Ubuntu,sans-serif;font-size:12px;color:var(--teal)}
.call .t2{font-family:Ubuntu,sans-serif;font-size:17px;font-weight:700;color:var(--teal)}
.ribbon{top:113px;width:24px;height:40px;background:#111}
.nav{left:49px;top:103px;width:822px;height:40px;background:var(--nav);display:flex;padding-left:269px}
.nav a{font-family:Ubuntu,sans-serif;font-size:11.5px;color:#ddd;text-decoration:none;letter-spacing:.5px;height:40px;line-height:40px;padding:0 18px;border-right:1px dotted #555}
.nav a:last-child{border:none}
.nav a.active{background:#fff;color:#222;margin-top:-8px;height:44px;line-height:58px;padding:0 14px}
.panel{left:59px;top:143px;width:802px;height:967px;background:var(--cream)}
.banner{left:72px;top:152px;width:774px;height:170px;border:3px solid #fff;box-shadow:0 1px 4px #bbb;background:linear-gradient(90deg,#b99e7c,#e8dccb 45%,#f4efe6 70%,#e4d6c3)}
.crumb{left:81px;top:343px;font-size:10px;font-weight:bold;color:#222}
.crumb b{color:var(--orange);font-weight:normal}
.offer{left:72px;top:365px;width:774px;height:31px;border:1px solid #ddd6c4;border-radius:3px;background:#f7f5ec;font-size:9.5px;line-height:29px;padding-left:9px;font-style:italic;color:#444}
.offer strong{font-style:normal;color:var(--orange);font-size:11.5px;margin-right:4px}
.article{left:72px;width:508px}
.article h2{font-family:Ubuntu,sans-serif;font-size:14px;color:var(--orange);font-weight:700;margin-left:2px}
.article .by{font-family:Ubuntu,sans-serif;font-size:10px;font-style:italic;color:#444;margin:2px 0 10px 2px}
.article .photo{float:left;width:116px;height:78px;margin:-3px 14px 4px 0}
.article p{font-size:9.6px;line-height:14.4px;text-align:justify}
.article .more{text-align:right;color:var(--orange);font-size:9px;margin-top:4px;clear:both}
.rule{left:72px;width:508px;border-top:1px dotted #bbb}
.vline{left:608px;top:403px;height:527px;border-left:1px solid #ccc5b3}
.lead{left:630px;top:403px;width:215px}
.lead h3{font-family:Ubuntu,sans-serif;font-size:15px;font-weight:500;color:#444;margin:9px 0 0 44px}
.lead h3 em{font-style:normal;color:var(--orange)}
.lead .avatar{left:0;top:0;width:36px;height:38px;background:linear-gradient(#ddd,#888);border-radius:40% 40% 6px 6px}
.lead .u{margin:4px 0 0 44px;width:70px;border-top:2px solid #ccc}
.lead p{font-size:9.3px;line-height:11px;margin:8px 0 14px;text-align:justify}
.field{width:214px;height:20px;background:var(--field);color:#333;font-size:9.5px;line-height:20px;padding-left:7px;margin-top:7px;border:1px solid #e4e0d4}
.field.sel{display:flex;justify-content:space-between;padding:0}
.field.sel span{padding-left:7px}
.field.sel i{width:20px;border-left:1px solid #999;background:#ddd;display:flex;align-items:center;justify-content:center}
.field.area{height:59px;line-height:12px;padding-top:6px}
.submit{left:783px;top:666px;width:60px;height:20px;background:#111;color:#fff;font-size:9.5px;font-weight:bold;border-radius:3px;text-align:center;line-height:20px}
.adbrand{left:648px;top:686px;font-family:Ubuntu,sans-serif;font-size:16px;color:#555}
.adbox{left:643px;top:724px;width:201px;height:200px;border:1px solid var(--teal);background:#fff;padding:10px 6px 0 11px;font-family:Ubuntu,sans-serif;overflow:hidden}
.ad{height:61px}
.ad a{display:block;font-size:9px;line-height:11px;font-weight:700;color:var(--link);text-decoration:underline}
.ad p{font-size:8.2px;line-height:11px;color:#222;margin-top:1px}
.ad small{display:block;font-size:7.6px;line-height:10px;color:var(--green)}
.adfoot{left:0;bottom:0;width:199px;height:14px;display:flex;justify-content:space-between;align-items:center;background:#fff}
.adfoot .arr{display:flex;gap:3px;padding-left:3px}
.adfoot .arr span{width:11px;height:11px;background:#9ab}
.adfoot .arr span+span{background:var(--teal)}
.adfoot .info{background:var(--link);color:#fff;font-size:8px;padding:2px 8px;border-radius:8px 0 0 0}
.deg-title{left:121px;top:958px;font-family:Ubuntu,sans-serif;font-size:15px;color:#444}
.deg-title em{font-style:normal;color:var(--orange)}
.deg-title:after{content:"";position:absolute;left:45px;top:24px;width:70px;border-top:2px solid #ccc}
.degrees{left:81px;top:992px;width:757px;height:105px;border:3px solid #fff;border-radius:5px;background:#e7e5df;box-shadow:0 0 2px #bbb}
.cert{top:11px;width:96px;height:72px;border:4px solid;background:#f5f2e6}
.footer{left:0;top:1110px;width:920px;height:90px;background:var(--footer)}
.flogo{left:72px;top:40px;font-family:Ubuntu,sans-serif;font-size:22px;color:#ddd;display:flex;align-items:center;gap:7px}
.flogo .mark{width:14px;height:14px;background:#999}
.flinks{left:290px;top:32px;font-size:10px;color:#ccc;word-spacing:2px}
.flinks span{margin:0 7px}
.copy{left:291px;top:48px;font-size:10px;color:#ccc}
.addr{right:74px;top:15px;font-size:10px;line-height:16px;color:#bbb;text-align:right}
.addr b{color:#bbb}
</style>
</head>
<body>
<header class="abs header">
  <div class="abs logo"><span class="mark"></span>Study Lantern</div>
  <div class="abs follow">Follow Us on : <span class="sq"></span><span class="sq"></span><span class="sq"></span></div>
  <div class="abs call">
    <div class="icon"><svg width="22" height="24" viewBox="0 0 22 24"><rect x="2" y="1" width="18" height="22" rx="3" fill="#fff"/><rect x="6" y="5" width="10" height="4" fill="#e1491d"/><g fill="#e1491d"><rect x="6" y="11" width="3" height="2"/><rect x="10" y="11" width="3" height="2"/><rect x="6" y="15" width="3" height="2"/><rect x="10" y="15" width="3" height="2"/></g></svg></div>
    <div><div class="t1">CALL US TOLL-FREE</div><div class="t2">123 .456 .7890</div></div>
  </div>
</header>

<div class="abs ribbon" style="left:27px"></div>
<div class="abs ribbon" style="left:869px"></div>
<nav class="abs nav">
  <a href="#">HOME</a><a href="#">ABOUT US</a><a href="#" class="active">ARTICLES</a><a href="#">DEGREES</a><a href="#">FAQ’S</a><a href="#">CONTACT US</a>
</nav>

<div class="abs panel"></div>
<div class="abs banner" role="img" aria-label="Sepia photo of an ink bottle, dip pen and spiral notebook with the word Articles in script"></div>

<div class="abs crumb">Home &nbsp;▸&nbsp; <b>Articles ▾</b></div>
<div class="abs offer"><strong>Latest Offer :</strong> Donec et dolor ac dui suscipit pellentesque. Pellentesque habitant morbi tristique senectus et netus et malesuada fames ac turpis egestas.</div>

<article class="abs article" style="top:426px">
  <h2>Etiam a neque non enim rhoncus rhoncus.</h2>
  <div class="by">By Mara Ellison</div>
  <div class="photo" role="img" aria-label="Graduate receiving a rolled diploma" style="background:linear-gradient(135deg,#2a2520,#b9a78e 60%,#e8dcc8)"></div>
  <p>Curabitur mattis sem tincidunt arcu gravida aliquet. In hac habitasse platea dictumst. Class aptent taciti sociosqu ad litora torquent per conubia nostra, per inceptos himenaeos. Quisque nisi risus, varius et sodales vitae, imperdiet vel sapien. In et est a elit luctus lacinia eu vel sapien. Mauris pulvinar venenatis elit nec egestas. Proin hendrerit euismod velit, non imperdiet dolor aliquam et. Nullam id nulla vitae sem congue ultrices eu id sapien.</p>
  <p style="margin-top:5px">Proin hendrerit euismod velit, non imperdiet dolor aliquam et. Nullam id nulla vitae sem congue ultrices eu id sapien. Donec et dolor ac dui suscipit pellentesque.</p>
  <div class="more">[+]</div>
</article>
<div class="abs rule" style="top:602px"></div>

<article class="abs article" style="top:619px">
  <h2>Etiam a neque non enim rhoncus rhoncus.</h2>
  <div class="by">By Mara Ellison</div>
  <div class="photo" role="img" aria-label="Student working on a laptop by a window" style="background:linear-gradient(135deg,#6f8f55,#d9d6cc 50%,#2b2b2b)"></div>
  <p>Curabitur mattis sem tincidunt arcu gravida aliquet. In hac habitasse platea dictumst. Class aptent taciti sociosqu ad litora torquent per conubia nostra, per inceptos himenaeos. Quisque nisi risus, varius et sodales vitae, imperdiet vel sapien. In et est a elit luctus lacinia eu vel sapien. Mauris pulvinar venenatis elit nec egestas. Proin hendrerit euismod velit, non imperdiet dolor aliquam et. Nullam id nulla vitae sem congue ultrices eu id sapien.</p>
  <div class="more">[+]</div>
</article>
<div class="abs rule" style="top:757px"></div>

<article class="abs article" style="top:772px">
  <h2>Etiam a neque non enim rhoncus rhoncus.</h2>
  <div class="by">By Mara Ellison</div>
  <div class="photo" role="img" aria-label="Student working on a laptop by a window" style="background:linear-gradient(135deg,#6f8f55,#d9d6cc 50%,#2b2b2b)"></div>
  <p>Curabitur mattis sem tincidunt arcu gravida aliquet. In hac habitasse platea dictumst. Class aptent taciti sociosqu ad litora torquent per conubia nostra, per inceptos himenaeos. Quisque nisi risus, varius et sodales vitae, imperdiet vel sapien. In et est a elit luctus lacinia eu vel sapien. Mauris pulvinar venenatis elit nec egestas. Proin hendrerit euismod velit, non imperdiet dolor aliquam et. Nullam id nulla vitae sem congue ultrices eu id sapien.</p>
  <div class="more">[+]</div>
</article>

<div class="abs vline"></div>

<aside class="abs lead">
  <div class="abs avatar" role="img" aria-label="Person icon"></div>
  <h3>Lead <em>Form</em></h3>
  <div class="u"></div>
  <p>Send us a quick email with any questions or concerns you may have about your potential case.</p>
  <div class="field">Your Name</div>
  <div class="field">Your Email Address</div>
  <div class="field">Your Phone No.</div>
  <div class="field sel"><span>Interested In</span><i><svg width="7" height="4"><path d="M0 0h7L3.5 4z" fill="#333"/></svg></i></div>
  <div class="field area">Provide Your Education Details.</div>
</aside>
<div class="abs submit">Submit</div>

<div class="abs adbrand">AdLink Network</div>
<div class="abs adbox">
  <div class="ad"><a>Affordable Hotels</a><p>Special rates until the end of the month. No booking fees.</p><small>www.example.com</small></div>
  <div class="ad"><a>Dublin Hotels</a><p>Browse 100+ hotels in Dublin, sort by price &amp; location.</p><small>www.example.com</small></div>
  <div class="ad"><a>Hotels in Ireland</a><p>Compare prices of 1000s of hotels all over ireland.</p><small>www.example.com</small></div>
  <div class="abs adfoot"><div class="arr"><span></span><span></span></div><div class="info">Ad Info ▷</div></div>
</div>

<div class="abs deg-title">List of <em>degrees</em></div>
<div class="abs degrees">
  <div class="abs cert" style="left:15px;border-color:#6b2a3e"></div>
  <div class="abs cert" style="left:135px;border-color:#f1ead6"></div>
  <div class="abs cert" style="left:255px;border-color:#8fa9d4"></div>
  <div class="abs cert" style="left:377px;border-color:#c99a6a"></div>
  <div class="abs cert" style="left:501px;border-color:#555;background:#d8d8d8"></div>
  <div class="abs cert" style="left:624px;border-color:#bbb"></div>
</div>

<footer class="abs footer">
  <div class="abs flogo"><span class="mark"></span>Study Lantern</div>
  <div class="abs flinks">Home<span>|</span>About Us<span>|</span>Services<span>|</span>Degrees<span>|</span>FAQs<span>|</span>Contact</div>
  <div class="abs copy">Copyright © 2011 - studylantern - All rights reserved. Terms and Privacy Policy</div>
  <div class="abs addr"><b>Address Line 1 with City</b><br><b>Address Line 2 with Country</b><br>Tel. : 123 . 456 . 7890<br>Email : info@studylantern.com</div>
</footer>
</body>
</html>
```